Revamp Business Card for Landscaping/Gardening Service Provider

We are a small landscaping company that is in desperate need of someone to recreate our business card. I have attached what we are currently using along with the logo.

These are the services we specialize in:
- lawn service
- mow, edge and clean
- fertilizing
- prune and trim
- seed and topping
- planting
- irrigation sprinklers

We don't want the front to be too busy but we do want the bulk of the information to be on this side such as the logo (recreate if possible), what we do and maybe the contact information. The back we would like it to be lined if possible, to add notes or even provide quotes for customers. If you feel you've got the talent to take on this project, please send in your design.

Thank you

```html
<!DOCTYPE html>
<html lang="en">
<head>
<meta charset="utf-8">
<title>Ortiz Green Gardening – Business Card</title>
<link href="https://fonts.googleapis.com/css2?family=Lato:wght@400;700&display=swap" rel="stylesheet">
<style>
  :root {
    --backdrop: #e6e7e8;
    --card-dark: #050505;
    --card-green: #3f6b22;
    --leaf: #3aa84a;
    --white: #ffffff;
    --rule: rgba(255,255,255,0.55);
    --bullet-front: #3aa84a;
    --band-light: #8fb06e;
    --band-mid: #6f9a4c;
    --shadow: rgba(0,0,0,0.35);
  }
  * { margin: 0; padding: 0; box-sizing: border-box; }
  html, body { width: 1200px; height: 1028px; overflow: hidden; }
  body {
    background: var(--backdrop);
    font-family: "Lato", Arial, sans-serif;
    position: relative;
  }
  .card {
    position: absolute;
    left: 260px;
    width: 619px;
    height: 364px;
    overflow: hidden;
    box-shadow: 6px 8px 10px var(--shadow);
  }
  .card-front { top: 85px; background: var(--card-dark); color: var(--white); }
  .card-back { top: 523px; background: var(--card-green); color: var(--white); }

  /* front */
  .tree-decoration {
    position: absolute; right: 0; top: 0;
    width: 210px; height: 364px;
    background: radial-gradient(ellipse at 60% 35%, #2a2a2a 0%, #171717 45%, var(--card-dark) 78%);
  }
  .owner-names {
    position: absolute; left: 62px; top: 28px;
    font-size: 22px; font-weight: 400;
    padding-bottom: 3px;
    border-bottom: 1.5px solid var(--white);
  }
  .brand {
    position: absolute; left: 40px; top: 112px; width: 232px;
    text-align: center;
  }
  .brand-rule { display: block; height: 2px; background: var(--white); margin: 0 8px; }
  .brand-name {
    display: block;
    font-weight: 700; font-size: 25px; line-height: 1.2;
    letter-spacing: 0.5px; text-transform: uppercase;
    color: var(--white);
    padding: 8px 0;
  }
  .brand-mark {
    display: block; width: 13px; height: 13px; border-radius: 50%;
    background: var(--leaf); margin: 10px auto 0;
  }
  .divider {
    position: absolute; left: 300px; top: 64px;
    width: 1px; height: 186px; background: rgba(255,255,255,0.4);
  }
  .service-list {
    position: absolute; left: 330px; top: 60px;
    list-style: none; font-size: 18px; line-height: 27px;
  }
  .service-list li { position: relative; padding-left: 22px; }
  .service-list li::before {
    content: ""; position: absolute; left: 0; top: 9px;
    width: 9px; height: 9px; border-radius: 50%; background: var(--bullet-front);
  }
  .contact {
    position: absolute; font-size: 16px; line-height: 20px;
    display: flex; align-items: center; gap: 12px;
  }
  .contact svg { width: 15px; height: 15px; fill: var(--leaf); flex: none; }
  .contact-phone { left: 28px; top: 280px; }
  .contact-email { left: 28px; top: 308px; }
  .contact-web { left: 338px; top: 308px; }

  /* back */
  .back-header {
    position: absolute; left: 40px; right: 40px; top: 26px;
    display: flex; justify-content: space-between; align-items: baseline;
  }
  .back-brand { font-size: 20px; font-weight: 700; letter-spacing: 0.5px; text-transform: uppercase; }
  .notes-label { font-size: 16px; font-weight: 400; letter-spacing: 1px; text-transform: uppercase; }
  .note-lines {
    position: absolute; left: 40px; right: 40px; top: 66px;
    list-style: none;
  }
  .note-lines li { height: 34px; border-bottom: 1px solid var(--rule); }
  .wave { position: absolute; left: 0; bottom: 0; width: 619px; height: 80px; }
</style>
</head>
<body>
  <section class="card card-front">
    <div class="tree-decoration" role="img" aria-label="Faint tree silhouette decoration"></div>
    <p class="owner-names">Ramon &amp; Elena Ortiz</p>

    <div class="brand">
      <span class="brand-rule"></span>
      <span class="brand-name">Ortiz Green<br>Gardening</span>
      <span class="brand-rule"></span>
      <span class="brand-mark"></span>
    </div>

    <div class="divider"></div>
    <ul class="service-list">
      <li>Lawn Service</li>
      <li>Mow, Edge &amp; Clean</li>
      <li>Fertilizing</li>
      <li>Prune &amp; Trim</li>
      <li>Seed &amp; Topping</li>
      <li>Planting</li>
      <li>Irrigation Sprinklers</li>
    </ul>

    <p class="contact contact-phone">
      <svg viewBox="0 0 24 24"><path d="M6.6 10.8a15.1 15.1 0 0 0 6.6 6.6l2.2-2.2c.3-.3.7-.4 1-.2 1.1.4 2.3.6 3.6.6.6 0 1 .4 1 1V20c0 .6-.4 1-1 1A17 17 0 0 1 3 4c0-.6.4-1 1-1h3.5c.6 0 1 .4 1 1 0 1.3.2 2.5.6 3.6.1.3 0 .7-.2 1z"/></svg>
      555 014 2290
    </p>
    <p class="contact contact-email">
      <svg viewBox="0 0 24 24"><path d="M2 5h20v14H2z"/><path d="M2 5l10 7 10-7" fill="none" stroke="#050505" stroke-width="2"/></svg>
      info@ortizgreengardening.com
    </p>
    <p class="contact contact-web">
      <svg viewBox="0 0 24 24"><circle cx="12" cy="12" r="10"/><path d="M2 12h20M12 2c3 3 3 17 0 20M12 2c-3 3-3 17 0 20" fill="none" stroke="#050505" stroke-width="1.5"/></svg>
      www.ortizgreengardening.com
    </p>
  </section>

  <section class="card card-back">
    <div class="back-header">
      <p class="back-brand">Ortiz Green Gardening</p>
      <p class="notes-label">Notes &amp; Quotes</p>
    </div>
    <ul class="note-lines" aria-label="Lined area for notes">
      <li></li><li></li><li></li><li></li><li></li><li></li>
    </ul>
    <svg class="wave" viewBox="0 0 619 80" preserveAspectRatio="none" aria-hidden="true">
      <path d="M0 62 C180 40 380 10 619 6 L619 80 L0 80 Z" fill="var(--band-light)"/>
      <path d="M0 66 C200 48 400 22 619 18 L619 80 L0 80 Z" fill="var(--band-mid)"/>
      <path d="M0 70 C200 56 420 30 619 28 L619 80 L0 80 Z" fill="var(--white)"/>
    </svg>
  </section>
</body>
</html>
```